Bref créative
quenzol stationary design
Stationary design
Modern
Ling Paoshen
Manager
52/3F Tanshu Road, Taipei,Taiwan
ling@quenzol.com
quenzol.com
I will like to have 12 sheeps jumping around and the design can derive from my logo. We can have characters such as 1: happy / laughing, 2: surprissed, 3: angry, 5: mysterious, 6: hurry and impatient, 7: affraid / chicken-hearted; cowardly, 8: Strong and muscular,
9: brave. Personalities that are fun .
Jumping sheeps

```html
<!DOCTYPE html>
<html lang="en">
<head>
<meta charset="utf-8">
<title>quenzol stationery</title>
<link href="https://fonts.googleapis.com/css2?family=Nunito:wght@400;700;800&display=swap" rel="stylesheet">
<style>
  :root {
    --bg: #e7e2da;
    --paper: #ffffff;
    --navy: #2e3d62;
    --ink: #4a4f5c;
    --muted: #9aa0ab;
    --faint: #e9ebef;
    --ghost: #eef0f3;
    --rule: #c9cdd4;
    --label: #5b5148;
  }
  * { box-sizing: border-box; margin: 0; padding: 0; }
  html, body { width: 1200px; height: 439px; overflow: hidden; }
  body { background: var(--bg); font-family: "Nunito", sans-serif; color: var(--ink); position: relative; }

  .sheet { position: absolute; top: 36px; width: 192px; height: 328px; background: var(--paper);
    box-shadow: 0 2px 6px rgba(0,0,0,.18); overflow: hidden; }
  .letterhead--one { left: 36px; }
  .letterhead--two { left: 310px; }
  .fax { left: 564px; }

  .brand { position: absolute; display: flex; align-items: center; gap: 4px; font-weight: 800; color: var(--navy); white-space: nowrap; }
  .brand__dot { width: 10px; height: 10px; border-radius: 50%; background: var(--navy); flex: none; }
  .sheet .brand { left: 12px; top: 12px; font-size: 11px; }

  /* faint scattered sheep characters, shown as soft tonal spots */
  .sheep-spot { position: absolute; border-radius: 50%;
    background: radial-gradient(circle, var(--faint) 0%, #f3f4f6 60%, rgba(255,255,255,0) 72%); }
  .sheep-spot--s { width: 26px; height: 22px; }
  .sheep-spot--l { width: 96px; height: 90px; }
  .ghost-name { position: absolute; left: 0; right: 0; top: 216px; text-align: center;
    font-size: 38px; font-weight: 800; color: var(--ghost); letter-spacing: -0.5px; }

  .footer-line { position: absolute; left: 8px; right: 8px; bottom: 14px; font-size: 4.5px; color: var(--muted);
    text-align: center; white-space: nowrap; }
  .footer-band { position: absolute; left: 0; right: 0; bottom: 0; height: 14px; background: var(--navy);
    color: #fff; font-size: 4.5px; display: flex; align-items: center; justify-content: center; white-space: nowrap; }

  .fax__contact { position: absolute; right: 12px; top: 10px; font-size: 4.5px; line-height: 6.5px; color: var(--muted); }
  .fax__title { position: absolute; left: 12px; top: 104px; font-size: 16px; font-weight: 700; color: var(--ink); }
  .fax__fields { position: absolute; left: 12px; right: 12px; top: 128px; display: grid;
    grid-template-columns: 1fr 1fr; column-gap: 12px; row-gap: 9px; }
  .field { font-size: 4.5px; color: var(--ink); border-bottom: 0.8px solid var(--rule); padding-bottom: 2px; }
  .fax__checks { position: absolute; left: 12px; right: 12px; top: 196px; display: flex;
    justify-content: space-between; font-size: 3.8px; color: var(--ink); white-space: nowrap; }
  .check { display: flex; align-items: center; gap: 2px; }
  .check::before { content: ""; width: 5px; height: 5px; border: 0.7px solid var(--ink); }

  .envelope { position: absolute; background: var(--paper); box-shadow: 0 2px 6px rgba(0,0,0,.2); overflow: hidden; }
  .envelope--back { left: 845px; top: 53px; width: 283px; height: 130px; }
  .envelope--back .flap { position: absolute; left: 0; right: 0; top: 0; height: 30px; background: var(--navy); }
  .envelope--front { left: 828px; top: 100px; width: 288px; height: 140px; }
  .envelope--front .brand { left: 12px; top: 12px; font-size: 10px; }
  .envelope--front .brand--center { left: 140px; top: 58px; font-size: 9px; }
  .envelope--front .band { position: absolute; left: 0; right: 0; bottom: 0; height: 10px; background: var(--navy); }
  .envelope__address { position: absolute; left: 12px; bottom: 14px; font-size: 4.2px; color: var(--muted); white-space: nowrap; }

  .card { position: absolute; background: var(--paper); box-shadow: 0 1px 4px rgba(0,0,0,.2); overflow: hidden; }
  .card .brand { font-size: 7.5px; left: 6px; top: 8px; gap: 3px; }
  .card .brand__dot { width: 7px; height: 7px; }
  .card--front { left: 883px; top: 305px; width: 100px; height: 44px; }
  .card--back { left: 996px; top: 305px; width: 100px; height: 44px; }
  .card--back .sheep-spot { right: 6px; top: 6px; width: 30px; height: 30px; }
  .card__person { position: absolute; left: 6px; bottom: 6px; font-size: 4.2px; line-height: 5.5px; color: var(--ink); white-space: nowrap; }
  .card--navy { left: 917px; top: 356px; width: 92px; height: 28px; background: var(--navy); }
  .card--navy .brand { color: #fff; left: 10px; top: 9px; }
  .card--navy .brand__dot { background: #fff; }

  .option-label { position: absolute; top: 376px; width: 192px; text-align: center; font-size: 12px; color: var(--label); }
</style>
</head>
<body>
  <section class="sheet letterhead letterhead--one">
    <div class="brand"><span class="brand__dot"></span>quenzol</div>
    <div class="sheep-spot sheep-spot--s" style="left:70px;top:40px" role="img" aria-label="Faint jumping sheep"></div>
    <div class="sheep-spot sheep-spot--s" style="left:118px;top:58px" role="img" aria-label="Faint jumping sheep"></div>
    <div class="sheep-spot sheep-spot--s" style="left:150px;top:28px" role="img" aria-label="Faint jumping sheep"></div>
    <div class="sheep-spot sheep-spot--s" style="left:40px;top:78px" role="img" aria-label="Faint jumping sheep"></div>
    <div class="sheep-spot sheep-spot--s" style="left:140px;top:96px" role="img" aria-label="Faint jumping sheep"></div>
    <div class="sheep-spot sheep-spot--s" style="left:150px;top:150px" role="img" aria-label="Faint jumping sheep"></div>
    <div class="sheep-spot sheep-spot--s" style="left:120px;top:190px" role="img" aria-label="Faint jumping sheep"></div>
    <div class="sheep-spot sheep-spot--l" style="left:10px;top:118px" role="img" aria-label="Large faint sheep character"></div>
    <div class="ghost-name">quenzol</div>
    <p class="footer-line">52/3F Tanshu Road, Taipei, Taiwan · ling@quenzol.com · quenzol.com</p>
  </section>
  <div class="option-label" style="left:36px">Option-1</div>

  <section class="sheet letterhead letterhead--two">
    <div class="brand"><span class="brand__dot"></span>quenzol</div>
    <div class="sheep-spot sheep-spot--s" style="left:70px;top:40px" role="img" aria-label="Faint jumping sheep"></div>
    <div class="sheep-spot sheep-spot--s" style="left:118px;top:58px" role="img" aria-label="Faint jumping sheep"></div>
    <div class="sheep-spot sheep-spot--s" style="left:150px;top:28px" role="img" aria-label="Faint jumping sheep"></div>
    <div class="sheep-spot sheep-spot--s" style="left:40px;top:78px" role="img" aria-label="Faint jumping sheep"></div>
    <div class="sheep-spot sheep-spot--s" style="left:140px;top:96px" role="img" aria-label="Faint jumping sheep"></div>
    <div class="sheep-spot sheep-spot--s" style="left:150px;top:150px" role="img" aria-label="Faint jumping sheep"></div>
    <div class="sheep-spot sheep-spot--s" style="left:120px;top:190px" role="img" aria-label="Faint jumping sheep"></div>
    <div class="sheep-spot sheep-spot--l" style="left:10px;top:118px" role="img" aria-label="Large faint sheep character"></div>
    <div class="ghost-name">quenzol</div>
    <div class="footer-band">52/3F Tanshu Road, Taipei, Taiwan · ling@quenzol.com · quenzol.com</div>
  </section>
  <div class="option-label" style="left:310px">Option-2</div>

  <section class="sheet fax">
    <div class="brand"><span class="brand__dot"></span>quenzol</div>
    <div class="fax__contact">52/3F Tanshu Road<br>Taipei, Taiwan<br>ling@quenzol.com<br>quenzol.com</div>
    <h1 class="fax__title">FAX</h1>
    <div class="fax__fields">
      <span class="field">To:</span><span class="field">From:</span>
      <span class="field">Fax:</span><span class="field">Pages:</span>
      <span class="field">Phone:</span><span class="field">Date:</span>
      <span class="field">Re:</span><span class="field">CC:</span>
    </div>
    <div class="fax__checks">
      <span class="check">Urgent</span><span class="check">For Review</span><span class="check">Please Comment</span><span class="check">Please Reply</span><span class="check">Please Recycle</span>
    </div>
  </section>
  <div class="option-label" style="left:564px">Option-3</div>

  <section class="envelope envelope--back"><div class="flap"></div></section>
  <section class="envelope envelope--front">
    <div class="brand"><span class="brand__dot"></span>quenzol</div>
    <div class="brand brand--center"><span class="brand__dot"></span>quenzol</div>
    <p class="envelope__address">52/3F Tanshu Road, Taipei, Taiwan</p>
    <div class="band"></div>
  </section>

  <section class="card card--front">
    <div class="brand"><span class="brand__dot"></span>quenzol</div>
    <p class="card__person">quenzol.com</p>
  </section>
  <section class="card card--back">
    <div class="brand"><span class="brand__dot"></span>quenzol</div>
    <div class="sheep-spot" role="img" aria-label="Faint sheep character"></div>
    <p class="card__person"><strong>Ling Paoshen</strong> · Manager<br>ling@quenzol.com</p>
  </section>
  <section class="card card--navy">
    <div class="brand"><span class="brand__dot"></span>quenzol</div>
  </section>
</body>
</html>
```